Namecard, letterhead & envelope
Executive Search firm
Project: Namecard, letterhead & envelope
Namecard, letterhead & envelope - Employment
Creative Brief
Professional
Derek Lim Wei Khong
President & CEO
548 Harbour Lane #05-07 Crestview Singapore 208463
dereklim@velquarepartners.example
www.velquarepartners.example
27K9053
If you think you can design a better logo, please feel free to do so. Your design should be clean, classy & professional looking. We are in the high-end headhuntng business. Background colour is white and preferably 2 colour, i.e. black plus one other colour, either gold or colour close to earth tone. But I am open to orange, yellow, brown.

```html
<!DOCTYPE html>
<html lang="en">
<head>
<meta charset="utf-8">
<title>Velquare Envelope</title>
<link rel="stylesheet" href="https://fonts.googleapis.com/css2?family=Roboto+Condensed:wght@400;700&display=swap">
<style>
  :root {
    --brand-red: #c3161c;
    --ink: #111111;
    --paper: #ffffff;
    --window-edge: #b9b9b9;
  }
  * { margin: 0; padding: 0; box-sizing: border-box; }
  html, body {
    width: 1200px;
    height: 600px;
    overflow: hidden;
    background: var(--paper);
  }
  .envelope {
    position: relative;
    width: 1200px;
    height: 600px;
    background: var(--paper);
  }
  .sender {
    position: absolute;
    left: 34px;
    top: 34px;
  }
  .sender-name {
    display: flex;
    align-items: center;
    gap: 14px;
    font-family: "Roboto Condensed", Arial, sans-serif;
    font-weight: 700;
    font-size: 54px;
    line-height: 1;
    color: var(--ink);
  }
  .sender-mark {
    width: 26px;
    height: 26px;
    background: var(--brand-red);
    flex: none;
  }
  .sender-tagline {
    margin-top: 12px;
    padding-left: 40px;
    font-family: "Roboto Condensed", Arial, sans-serif;
    font-weight: 400;
    font-size: 24px;
    line-height: 1.2;
    color: var(--ink);
    letter-spacing: 0.3px;
  }
  .address-window {
    position: absolute;
    left: 24px;
    top: 300px;
    width: 588px;
    height: 174px;
    border: 4px solid var(--window-edge);
    border-radius: 24px;
    background: var(--paper);
    box-shadow: inset 0 0 34px 10px rgba(0, 0, 0, 0.38);
  }
  .footer-band {
    position: absolute;
    left: 20px;
    right: 0;
    top: 533px;
    height: 48px;
    background: var(--brand-red);
    display: flex;
    align-items: center;
    justify-content: flex-end;
    padding-right: 18px;
  }
  .footer-web {
    font-family: "Roboto Condensed", Arial, sans-serif;
    font-weight: 700;
    font-size: 32px;
    color: var(--paper);
    letter-spacing: 0.2px;
    white-space: nowrap;
  }
</style>
</head>
<body>
  <main class="envelope">
    <header class="sender">
      <div class="sender-name"><span class="sender-mark"></span>Velquare</div>
      <div class="sender-tagline">Executive Search International</div>
    </header>
    <div class="address-window" aria-label="Address window"></div>
    <footer class="footer-band">
      <span class="footer-web">www.velquarepartners.example</span>
    </footer>
  </main>
</body>
</html>
```